Website Required for Small Cyber Security Company

Require a website for Cyber Security company. I have logo which i will attach. Please use logo blue and white as a guide
Would ultimately like the site to have a technology theme with the following pages Landing page
Services
Contact
Careers

I can provide content for each of those pages in due course, until then happy for you to use dummy data to display purposes

Target Market(s)

Government

Industry/Entity Type

Cyber Security

Coding

Coded - Design and coding required

Number of Pages Required

4 page

Colors
0054AA
0677BA
7BADD7
CADEEF
E8F1F8

Requirements
Must have
• High quality finish and UX
Nice to have
• look and feel professional and not cheap

```html
<!DOCTYPE html>
<html lang="en">
<head>
<meta charset="utf-8">
<title>Harlow Ridge Consulting</title>
<link href="https://fonts.googleapis.com/css2?family=Ubuntu:wght@300;400;500;700&family=Open+Sans:wght@400;600;700&display=swap" rel="stylesheet">
<style>
:root{
  --navy:#0b1a33;
  --ink:#0e1b2c;
  --teal:#0fa8c9;
  --blue:#0054aa;
  --mist:#eef2f7;
  --line:#d7dde5;
  --muted:#6b7380;
  --white:#ffffff;
  --lilac:#c9c3f2;
}
*{box-sizing:border-box;margin:0;padding:0}
html,body{width:1200px;height:4352px;overflow:hidden}
body{position:relative;font-family:"Open Sans",sans-serif;color:var(--ink);background:var(--white)}
.abs{position:absolute}
.h{font-family:"Ubuntu",sans-serif}
.title-bold{font-family:"Ubuntu",sans-serif;font-weight:700}
.label{font-size:14px;color:var(--teal);letter-spacing:.3px;text-align:center;width:100%}
.label span{border-bottom:1px solid var(--teal);padding-bottom:4px}
.btn{display:flex;align-items:center;justify-content:center;gap:14px;background:var(--teal);color:var(--white);font-weight:700;font-size:16px;border-radius:2px}
.photo{border-radius:2px}

/* hero */
.hero{left:0;top:0;width:1200px;height:769px;background:linear-gradient(160deg,#46515c 0%,#222d38 45%,#0f1720 100%)}
.topbar{top:10px;font-size:12px;color:var(--white);display:flex;align-items:center;gap:6px}
.social{top:9px;width:14px;height:14px;background:var(--white);border-radius:2px}
.nav{left:83px;top:34px;width:1032px;height:86px;background:var(--white);border-radius:3px}
.brand{display:flex;align-items:center;gap:8px;font-family:"Ubuntu",sans-serif;font-weight:500;color:var(--navy)}
.brand i{display:block;border-radius:50%;border:3px solid var(--blue)}
.navlinks{left:348px;top:35px;display:flex;gap:66px;font-size:13px;color:var(--ink);letter-spacing:.4px}
.hero .kicker{top:326px;width:100%;text-align:center;color:var(--white);font-size:15px;font-weight:600}
.hero h1{top:352px;width:100%;text-align:center;color:var(--white);font-family:"Ubuntu",sans-serif;font-weight:300;font-size:82px;line-height:88px}

/* services */
.services{left:0;top:769px;width:1200px;height:681px;background:var(--mist)}
.card{top:214px;width:324px;height:254px;background:var(--white);border-radius:4px;box-shadow:0 4px 14px rgba(0,0,0,.06)}
.card .photo{position:absolute;left:18px;top:-30px;width:290px;height:163px}
.card .badge{position:absolute;left:240px;top:78px;width:52px;height:52px;border-radius:50%;background:var(--navy);display:flex;align-items:center;justify-content:center}
.card .small{position:absolute;top:185px;width:100%;text-align:center;font-size:11px;color:var(--teal)}
.card .title{position:absolute;top:200px;width:100%;text-align:center;font-family:"Ubuntu",sans-serif;font-size:28px}

/* about */
.about{left:0;top:1450px;width:1200px;height:558px;background:linear-gradient(110deg,#2b3440 0%,#1b2430 55%,#131b25 100%)}
.about p{color:#e6e9ee;font-size:13px;line-height:21px}

/* why */
.why{left:0;top:2008px;width:1200px;height:708px;background:var(--white)}
.feat h3{font-family:"Ubuntu",sans-serif;font-weight:400;font-size:20px;color:var(--ink);margin-bottom:8px}
.feat p{font-size:12.5px;line-height:21px;color:var(--muted);width:220px}
.ico{width:70px;height:70px;border-radius:50%;background:var(--navy);border:4px solid var(--white);box-shadow:0 0 0 1px var(--line);display:flex;align-items:center;justify-content:center}

/* testimonials */
.testi{left:0;top:2716px;width:1200px;height:554px;background:linear-gradient(180deg,#2a333d 0%,#1f2832 100%)}
.quote{top:189px;width:490px;height:188px;background:rgba(120,128,138,.45);border-radius:3px;padding:32px 20px}
.quote h4{font-family:"Ubuntu",sans-serif;font-weight:500;font-size:27px;color:var(--white);margin-bottom:12px}
.quote p{font-size:15px;line-height:24px;color:#eef0f3}
.quote:after{content:"";position:absolute;left:36px;bottom:-16px;border:16px solid transparent;border-bottom:0;border-top-color:rgba(120,128,138,.45)}
.who{display:flex;align-items:center;gap:26px;color:var(--white)}
.who .av{width:64px;height:64px;border-radius:50%;background:linear-gradient(135deg,#b9a58f,#3d4a58)}
.who b{font-family:"Ubuntu",sans-serif;font-weight:700;font-size:21px;display:block}
.who small{font-size:14px}

/* contact */
.contact{left:0;top:3270px;width:1200px;height:1026px}
.field{border:1px solid var(--line);border-radius:2px;font-size:11px;color:var(--muted);padding:8px}
.footer-nav{display:flex;gap:44px;color:var(--white);font-size:14px}
.info{display:flex;align-items:center;gap:20px;color:var(--white);font-size:12px;line-height:18px}
.info .c{width:56px;height:56px;border:1.5px solid var(--white);border-radius:50%;display:flex;align-items:center;justify-content:center}
.bottombar{left:0;top:4296px;width:1200px;height:56px;background:var(--teal)}
.sq{width:22px;height:22px;border:1px solid var(--white);border-radius:2px}
</style>
</head>
<body>

<!-- HERO -->
<section class="abs hero">
  <div class="abs photo" role="img" aria-label="Team of professionals working together in a bright modern office, dimmed" style="left:0;top:0;width:1200px;height:769px;background:radial-gradient(ellipse at 75% 30%,rgba(150,160,170,.35),transparent 55%),radial-gradient(ellipse at 15% 60%,rgba(120,130,140,.3),transparent 50%),linear-gradient(180deg,rgba(14,22,32,.25),rgba(14,22,32,.7))"></div>
  <div class="abs topbar" style="left:98px">
    <svg width="10" height="13" viewBox="0 0 10 13"><path d="M5 0a5 5 0 0 0-5 5c0 4 5 8 5 8s5-4 5-8a5 5 0 0 0-5-5z" fill="#fff"/><circle cx="5" cy="5" r="2" fill="#2a3440"/></svg>48 Harbour Lane , Eastfield</div>
  <div class="abs topbar" style="left:360px">
    <svg width="13" height="9" viewBox="0 0 13 9"><rect width="13" height="9" fill="#fff"/><path d="M0 0l6.5 5L13 0" stroke="#2a3440" fill="none"/></svg>hello@harlowridge.example</div>
  <div class="abs topbar" style="left:575px">
    <svg width="11" height="11" viewBox="0 0 11 11"><path d="M2 0l2 3-1 1.5a7 7 0 0 0 3.5 3.5L8 7l3 2-1 2C5 11 0 6 0 1z" fill="#fff"/></svg>555 - 014 - 2207</div>
  <div class="abs social" style="left:1000px"></div>
  <div class="abs social" style="left:1029px"></div>
  <div class="abs social" style="left:1057px"></div>
  <div class="abs social" style="left:1085px"></div>

  <nav class="abs nav">
    <div class="abs brand" style="left:34px;top:26px;font-size:14px"><i style="width:32px;height:32px"></i>HARLOW RIDGE</div>
    <div class="abs navlinks"><span>HOME</span><span>ABOUT US</span><span>SERVICES</span><span>CONTACT US</span></div>
  </nav>

  <div class="abs kicker">CYBERSECURITY SERVICES</div>
  <h1 class="abs">Unlocking the Power<br>of Cyber Protection</h1>
  <div class="abs btn" style="left:522px;top:592px;width:156px;height:45px">Contact us
    <svg width="18" height="12" viewBox="0 0 18 12"><path d="M0 6h16M11 1l5 5-5 5" stroke="#fff" stroke-width="1.6" fill="none"/></svg></div>
</section>

<!-- SERVICES -->
<section class="abs services">
  <div class="abs label" style="top:61px"><span>WHAT WE DO</span></div>
  <h2 class="abs title-bold" style="top:100px;width:100%;text-align:center;font-size:48px">Services We Offer</h2>

  <div class="abs card" style="left:85px">
    <div class="photo" role="img" aria-label="Hands on a laptop with glowing analytics icons" style="background:radial-gradient(circle at 70% 40%,#c8ccd0,transparent 45%),linear-gradient(135deg,#5a636d,#1f262e)"></div>
    <div class="badge"><svg width="24" height="24" viewBox="0 0 24 24" fill="none" stroke="#fff" stroke-width="1.6"><path d="M7 18h11a4 4 0 0 0 0-8 6 6 0 0 0-11.5 1.5A3.3 3.3 0 0 0 7 18z"/></svg></div>
    <div class="small">OUR SERVICES</div><div class="title">Cloud Security</div>
  </div>
  <div class="abs card" style="left:436px">
    <div class="photo" role="img" aria-label="Hand on a computer mouse with a glowing blue cloud network" style="background:radial-gradient(circle at 65% 40%,#2a9fd0,transparent 45%),linear-gradient(135deg,#0e4f7a,#071a2e)"></div>
    <div class="badge"><svg width="24" height="24" viewBox="0 0 24 24" fill="none" stroke="#fff" stroke-width="1.6"><circle cx="12" cy="12" r="8"/><path d="M12 7v5l3 3"/></svg></div>
    <div class="small">OUR SERVICES</div><div class="title">Incident Response</div>
  </div>
  <div class="abs card" style="left:788px">
    <div class="photo" role="img" aria-label="Two colleagues reviewing work at a desktop computer" style="background:linear-gradient(135deg,#d8dadd,#8a8f96 55%,#3d4248)"></div>
    <div class="badge"><svg width="24" height="24" viewBox="0 0 24 24" fill="none" stroke="#fff" stroke-width="1.6"><path d="M12 3l7 3v5c0 4.5-3 8-7 10-4-2-7-5.5-7-10V6z"/><path d="M9 12l2 2 4-4"/></svg></div>
    <div class="small">OUR SERVICES</div><div class="title">Network Security</div>
  </div>

  <div class="abs" style="top:524px;width:100%;text-align:center;font-size:18px;color:var(--muted)">The demanded experts in your area</div>
  <div class="abs btn" style="left:488px;top:569px;width:218px;height:65px;background:var(--white);color:var(--teal);font-size:23px;font-weight:600;gap:24px">Contact us
    <svg width="26" height="16" viewBox="0 0 26 16"><path d="M0 8h24M17 1l7 7-7 7" stroke="#0fa8c9" stroke-width="2" fill="none"/></svg></div>
</section>

<!-- ABOUT -->
<section class="abs about">
  <div class="abs" style="left:100px;top:82px;width:400px;height:380px;background:#0e2440;border-radius:36px;transform:rotate(-7deg)"></div>
  <div class="abs photo" role="img" aria-label="Two business colleagues reviewing a tablet in an office" style="left:112px;top:88px;width:382px;height:372px;border-radius:36px;background:radial-gradient(ellipse at 55% 45%,#e3e6ea,transparent 40%),linear-gradient(135deg,#8c96a1,#2d3640)"></div>

  <div class="abs" style="left:612px;top:60px;font-size:12px;color:var(--white);font-weight:600;border-bottom:1px solid var(--white);padding-bottom:3px">WHO WE ARE</div>
  <h2 class="abs title-bold" style="left:612px;top:94px;font-size:44px;line-height:51px;color:var(--white)">Defending Your Digital<br>Frontier</h2>
  <div class="abs h" style="left:612px;top:226px;font-size:21px;color:var(--white);font-weight:500">Your Partner in Cybersecurity Success.</div>
  <p class="abs" style="left:612px;top:269px;width:505px">Lorem ipsum dolor sit amet, consectetur adipiscing elit, sed do eiusmod tempor incididunt ut labore et dolore magna aliqua. Ut enim ad minim veniam, quis laboris nisi ut aliquip ex ea commodo consequat.</p>
  <p class="abs" style="left:612px;top:345px;width:505px">Lorem ipsum dolor sit amet, consectetur adipiscing elit, sed do eiusmod tempor incididunt ut labore et dolore magna aliqua.</p>
  <div class="abs btn" style="left:610px;top:428px;width:156px;height:45px">Contact us
    <svg width="18" height="12" viewBox="0 0 18 12"><path d="M0 6h16M11 1l5 5-5 5" stroke="#fff" stroke-width="1.6" fill="none"/></svg></div>
</section>

<!-- WHY CHOOSE US -->
<section class="abs why">
  <div class="abs label" style="top:72px;font-size:11px"><span>WHY US</span></div>
  <h2 class="abs title-bold" style="top:104px;width:100%;text-align:center;font-size:34px">Why Choose Us</h2>

  <svg class="abs" style="left:412px;top:183px" width="400" height="400" viewBox="0 0 400 400">
    <circle cx="200" cy="200" r="183" fill="none" stroke="#0b1a33" stroke-width="1.4" stroke-dasharray="6 5"/>
    <circle cx="200" cy="200" r="148" fill="none" stroke="var(--lilac)" stroke-width="12"/>
  </svg>
  <div class="abs" role="img" aria-label="Portrait of a smiling businesswoman in a dark suit" style="left:480px;top:251px;width:264px;height:264px;border-radius:50%;background:linear-gradient(180deg,#eceef1 0%,#c7b39c 45%,#1e2633 75%)"></div>

  <div class="abs ico" style="left:409px;top:294px"><svg width="28" height="28" viewBox="0 0 24 24" fill="none" stroke="#fff" stroke-width="1.5"><path d="M12 3l7 3v5c0 4.5-3 8-7 10-4-2-7-5.5-7-10V6z"/><path d="M9 12l2 2 4-4"/></svg></div>
  <div class="abs ico" style="left:384px;top:394px"><svg width="28" height="28" viewBox="0 0 24 24" fill="none" stroke="#fff" stroke-width="1.5"><circle cx="12" cy="12" r="3"/><path d="M12 2v3M12 19v3M2 12h3M19 12h3M5 5l2 2M17 17l2 2M5 19l2-2M17 7l2-2"/></svg></div>
  <div class="abs ico" style="left:426px;top:492px"><svg width="28" height="28" viewBox="0 0 24 24" fill="none" stroke="#fff" stroke-width="1.5"><path d="M12 3l2.7 5.6 6.1.9-4.4 4.3 1 6.1L12 17l-5.4 2.9 1-6.1-4.4-4.3 6.1-.9z"/></svg></div>
  <div class="abs ico" style="left:727px;top:294px"><svg width="28" height="28" viewBox="0 0 24 24" fill="none" stroke="#fff" stroke-width="1.5"><rect x="5" y="3" width="14" height="18" rx="1"/><path d="M8 9h8M8 13h8M8 17h5"/></svg></div>
  <div class="abs ico" style="left:751px;top:394px"><svg width="28" height="28" viewBox="0 0 24 24" fill="none" stroke="#fff" stroke-width="1.5"><circle cx="12" cy="12" r="9"/><path d="M7.5 12l3 3 6-6"/></svg></div>
  <div class="abs ico" style="left:705px;top:492px"><svg width="28" height="28" viewBox="0 0 24 24" fill="none" stroke="#fff" stroke-width="1.5"><circle cx="12" cy="12" r="9"/><path d="M12 7v5l3 3"/></svg></div>

  <div class="abs feat" style="left:201px;top:293px"><h3>Cost-Effective</h3><p>Lorem ipsum dolor sit amet, consectetur adipiscing elit, sed do eiusmod tempor incididunt</p></div>
  <div class="abs feat" style="left:171px;top:407px"><h3>Client-Centric</h3><p>Lorem ipsum dolor sit amet, consectetur adipiscing elit, sed do eiusmod tempor incididunt</p></div>
  <div class="abs feat" style="left:201px;top:518px"><h3>Global Reach</h3><p>Lorem ipsum dolor sit amet, consectetur adipiscing elit, sed do eiusmod tempor incididunt</p></div>
  <div class="abs feat" style="left:833px;top:274px"><h3>Regulatory Compliance</h3><p>Lorem ipsum dolor sit amet, consectetur adipiscing elit, sed do eiusmod tempor incididunt</p></div>
  <div class="abs feat" style="left:852px;top:393px"><h3>Quality Assurance</h3><p>Lorem ipsum dolor sit amet, consectetur adipiscing elit, sed do eiusmod tempor incididunt</p></div>
  <div class="abs feat" style="left:808px;top:518px"><h3>Timely Delivery</h3><p>Lorem ipsum dolor sit amet, consectetur adipiscing elit, sed do eiusmod tempor incididunt</p></div>
</section>

<!-- TESTIMONIALS -->
<section class="abs testi">
  <div class="abs" style="left:90px;top:50px;font-size:12px;color:var(--white);font-weight:600;border-bottom:1px solid var(--white);padding-bottom:3px">TESTIMONIALS</div>
  <h2 class="abs title-bold" style="left:90px;top:84px;font-size:44px;color:var(--white)">What our clients are saying</h2>
  <div class="abs" style="left:916px;top:99px;font-size:15px;color:var(--white);font-weight:600">More Testimonials</div>
  <div class="abs" style="left:1065px;top:89px;width:37px;height:38px;background:var(--teal)">
    <svg width="37" height="38" viewBox="0 0 37 38"><path d="M16 13l6 6-6 6" stroke="#fff" stroke-width="2.4" fill="none"/></svg></div>

  <div class="abs quote" style="left:93px"><h4>Their service was excellent</h4><p>Lorem ipsum dolor sit amet, consectetur adipiscing elit, sed do eiusmod tempor incididunt ut labore et dolore magna aliqua. Ut enim ad minim</p></div>
  <div class="abs quote" style="left:615px"><h4>Their service was excellent</h4><p>Lorem ipsum dolor sit amet, consectetur adipiscing elit, sed do eiusmod tempor incididunt ut labore et dolore magna aliqua. Ut enim ad minim</p></div>

  <div class="abs who" style="left:110px;top:411px"><div class="av" role="img" aria-label="Client portrait"></div><div><b>Maren Holt</b><small>Client</small></div></div>
  <div class="abs who" style="left:632px;top:411px"><div class="av" role="img" aria-label="Client portrait"></div><div><b>Davis Crane</b><small>Client</small></div></div>

  <div class="abs" style="left:586px;top:517px;width:11px;height:11px;border-radius:50%;background:var(--teal)"></div>
  <div class="abs" style="left:608px;top:517px;width:11px;height:11px;border-radius:50%;background:var(--white)"></div>
  <div class="abs" style="left:631px;top:517px;width:11px;height:11px;border-radius:50%;background:var(--white)"></div>
</section>

<!-- CONTACT + FOOTER -->
<section class="abs contact">
  <svg class="abs" style="left:0;top:0" width="1200" height="1026" viewBox="0 0 1200 1026">
    <path d="M0 620 Q120 520 260 470 L940 470 Q1080 500 1200 590 L1200 1026 L0 1026 Z" fill="#1d2733"/>
    <path d="M1050 480 Q1140 510 1200 560" stroke="var(--teal)" stroke-width="26" fill="none"/>
  </svg>

  <div class="abs label" style="top:73px"><span>CONTACT US</span></div>
  <h2 class="abs title-bold" style="top:110px;width:100%;text-align:center;font-size:42px">Get in touch with us</h2>

  <div class="abs" style="left:139px;top:227px;width:921px;height:454px;background:var(--white);border-radius:6px;box-shadow:0 6px 24px rgba(0,0,0,.12)">
    <div class="abs photo" role="img" aria-label="Smiling man in a blue sweater holding a tablet" style="left:0;top:0;width:461px;height:454px;background:radial-gradient(ellipse at 45% 40%,#b49a82,transparent 30%),radial-gradient(ellipse at 45% 80%,#3e5a78,transparent 45%),linear-gradient(160deg,#4a5663,#1c2530)"></div>
    <div class="abs brand" style="left:514px;top:28px;font-size:16px"><i style="width:36px;height:36px"></i>HARLOW RIDGE</div>
    <div class="abs h" style="left:512px;top:110px;font-size:31px;font-weight:300;color:var(--navy)">Please fill out the form</div>
    <div class="abs field" style="left:512px;top:170px;width:360px;height:34px;border-width:0 0 1px 0">Name</div>
    <div class="abs field" style="left:512px;top:221px;width:172px;height:37px">Phone</div>
    <div class="abs field" style="left:698px;top:221px;width:174px;height:37px">Email</div>
    <div class="abs field" style="left:512px;top:274px;width:360px;height:69px">Message</div>
    <div class="abs btn" style="left:512px;top:360px;width:360px;height:38px;font-size:12px;border-radius:0">Send</div>
  </div>

  <div class="abs brand" style="left:516px;top:760px;font-size:19px;color:var(--white);flex-direction:column;gap:6px"><i style="width:48px;height:48px;border-color:var(--white)"></i>HARLOW RIDGE</div>
  <div class="abs footer-nav" style="left:352px;top:845px"><span>HOME</span><span>SERVICES</span><span>ABOUT US</span><span>TESTIMONIALS</span><span>BLOG</span></div>
  <div class="abs" style="left:143px;top:897px;width:917px;height:1px;background:rgba(255,255,255,.25)"></div>

  <div class="abs info" style="left:173px;top:941px"><div class="c">
    <svg width="30" height="30" viewBox="0 0 30 30" fill="none" stroke="#fff" stroke-width="1.5"><circle cx="15" cy="15" r="13"/><ellipse cx="15" cy="15" rx="6" ry="13"/><path d="M2 15h26M4 8h22M4 22h22"/></svg></div>
    <div>Unit 9, Quayside House<br>Eastfield, ST 40512</div></div>
  <div class="abs" style="left:431px;top:936px;width:1px;height:62px;background:rgba(255,255,255,.3)"></div>
  <div class="abs info" style="left:506px;top:941px"><div class="c">
    <svg width="20" height="30" viewBox="0 0 20 30" fill="none" stroke="#fff" stroke-width="1.5"><rect x="3" y="1" width="14" height="28" rx="2"/><path d="M8 25h4"/></svg></div>
    <div><span style="font-size:14px">PHONE</span><br>(555) 014 2207</div></div>
  <div class="abs" style="left:750px;top:936px;width:1px;height:62px;background:rgba(255,255,255,.3)"></div>
  <div class="abs info" style="left:828px;top:941px"><div class="c">
    <svg width="30" height="26" viewBox="0 0 30 26" fill="none" stroke="#fff" stroke-width="1.5"><rect x="1" y="7" width="28" height="18"/><path d="M1 7l14 10 14-10M6 10V2h18v8"/></svg></div>
    <div><span style="font-size:14px">EMAIL</span><br>info@harlowridge.example</div></div>
</section>

<div class="abs bottombar">
  <div class="abs" style="left:147px;top:19px;font-size:13px;color:var(--white);font-weight:600">Harlow Ridge Consulting</div>
  <div class="abs" style="left:932px;top:17px;display:flex;gap:12px"><div class="sq"></div><div class="sq"></div><div class="sq"></div><div class="sq"></div></div>
</div>

</body>
</html>
```